Millbrook Artisanal & Craft Beer ***

WordPress Website redesign for an existing site https://millbrookogunquit-example.com/ and https://millbrookportsmouth-example.com/ (currently broken). Only one site, We want the Portsmouth site to be the one created. There have been issues with it in the past which caused it to crash and just randomly loose data/not hold the installed code. We want it to look similar to the other site listed as they are one company with two locations. that's why we added both. The Ogt location is for reference only.
Client is a Pizza and craft beer Restaurant/Foodservice establishment in Riverton, NH USA. wanting to have a more secure site that is visually appealing, efficient, and easy for the staff to go in and adjust menu items periodically
both the Reservation and the Gift card tabs/button will link to external sites (tablyx.com, payvenly.com, with restaurant specific info) so they will need to be for design purpose only.

Target Market(s)

Restaurant Dining, Consumers

Industry/Entity Type

foodservice, Restaurant

Coding

Coded - Design and coding required

Number of Pages Required

5+ page

Colors

Designer to choose colors to be used in the design.

Requirements
Must have
• Menu that is easily accessible by customers on their phones from a QR code. Gift cards and online sales (need to be separate for companies) I like that the current site is one page that is scrollable with clicks to sections and it can be easily viewed n mobile phone. It should have sections: menu, reservations (link), order take out (link), buy gift cards (link), work here (with application form), Events/Private Parties, Data collection boilerplate legal statement? Must be easily editable by my staff so they can change menu items Needs to use our logo and branding better
Nice to have
• Can it collect emails for advertising purposes? Can this automatically go into a system that my staff can use?

```html
<!DOCTYPE html>
<html lang="en">
<head>
<meta charset="utf-8">
<title>Millbrook Artisanal Pizza &amp; Craft Beer</title>
<link rel="stylesheet" href="https://fonts.googleapis.com/css2?family=Barlow:wght@500;600;700;800&family=Arimo:wght@400;700&display=swap">
<style>
:root{
  --red:#d13a27;
  --ink:#222;
  --body:#444;
  --paper:#f1f1f1;
  --beige:#e9e3dc;
  --black:#000;
  --white:#fff;
}
*{margin:0;padding:0;box-sizing:border-box}
html,body{width:1200px;height:3931px;overflow:hidden}
body{position:relative;background:var(--paper);font-family:Arimo,Arial,sans-serif;color:var(--body)}
.abs{position:absolute}
.heading{font-family:Barlow,Arial,sans-serif;font-weight:600;color:var(--ink);text-transform:uppercase}
.rule{width:46px;height:4px;background:var(--red)}
.btn{position:absolute;display:flex;align-items:center;justify-content:center;font-family:Barlow,Arial,sans-serif;font-weight:600;font-size:16px;text-transform:uppercase;color:var(--white);background:var(--red)}
.btn-ghost{background:transparent;border:2px solid var(--white)}

.topbar{top:0;left:0;width:1200px;height:49px;background:var(--red);color:var(--white);font-size:12px;font-weight:700;display:flex;align-items:center;padding-left:105px}
.header{top:49px;left:0;width:1200px;height:73px;background:var(--beige)}
.brand{display:flex;flex-direction:column;align-items:center}
.brand-name{font-family:Barlow,Arial,sans-serif;font-weight:700;letter-spacing:3px;text-transform:uppercase}
.brand-tag{font-family:Barlow,Arial,sans-serif;font-weight:700;letter-spacing:1px}
.header .brand{left:100px;top:14px;width:200px}
.header .brand-name{font-size:17px;color:var(--ink);display:flex;align-items:center;gap:8px}
.header .brand-name i{display:block;width:10px;height:10px;background:var(--red)}
.header .brand-tag{font-size:10px;color:var(--ink);margin-top:4px}
.nav{display:flex;gap:45px;font-family:Arimo,Arial,sans-serif;font-size:13px;color:var(--ink);text-transform:uppercase}
.header .nav{left:368px;top:30px}
.phone-btn{left:934px;top:15px;width:165px;height:46px;font-size:17px}

.hero-bg{top:122px;left:0}
.hero-title{left:100px;top:282px;font-family:Barlow,Arial,sans-serif;font-weight:800;font-size:64px;line-height:66px;color:var(--white);text-transform:uppercase}
.hero-text{left:100px;top:433px;width:440px;font-size:14px;line-height:24px;color:var(--white)}
.hero-cta{left:98px;top:523px;width:168px;height:48px}

.about h2{position:absolute;top:813px;left:0;width:1200px;text-align:center;font-size:24px}
.about .rule{position:absolute;top:852px;left:577px}
.about p{position:absolute;top:870px;left:152px;width:896px;text-align:center;font-size:13px;line-height:27.3px}
.about-cta{left:517px;top:1055px;width:166px;height:46px}

.band-bg{top:1122px;left:0}
.band-col{position:absolute;top:1255px;text-align:center;color:var(--white)}
.band-col h2{font-family:Barlow,Arial,sans-serif;font-weight:600;font-size:33px;text-transform:uppercase;margin-bottom:14px;white-space:nowrap}
.band-col p{font-size:13px;line-height:25.6px}
.band-left{left:66px;width:460px}
.band-right{left:670px;width:468px}
.band-btn{width:168px;height:49px;top:1458px}

.career h2{position:absolute;left:108px;top:1722px;font-size:22px}
.career .rule{position:absolute;left:108px;top:1759px}
.career p{position:absolute;left:108px;top:1780px;width:446px;font-size:13px;line-height:27.2px;text-align:justify}
.career-cta{left:108px;top:2069px;width:166px;height:46px}
.career-frame{left:632px;top:1713px;width:460px;height:431px;border:2px solid var(--red)}
.career-photo{left:608px;top:1698px;width:459px;height:429px;background:linear-gradient(135deg,#5d4a37 0%,#8a6a46 35%,#c9a35f 55%,#3b2a1d 80%,#776659 100%)}

.locations-bg{top:2241px;left:0;width:1200px;height:752px;background:var(--beige)}
.locations h2{position:absolute;top:2316px;left:0;width:1200px;text-align:center;font-size:23px;line-height:33px}
.locations .rule{position:absolute;left:577px;top:2390px}
.locations p.lead{position:absolute;top:2407px;left:175px;width:850px;text-align:center;font-size:13px;line-height:27px}
.card{position:absolute;top:2509px;width:300px;height:357px;background:var(--white);box-shadow:0 2px 8px rgba(0,0,0,.12);text-align:center}
.card-photo{height:195px}
.card h3{font-family:Barlow,Arial,sans-serif;font-weight:600;font-size:16px;color:var(--ink);margin-top:22px}
.card .addr{font-size:13.5px;color:var(--ink);margin-top:13px}
.card .btn{left:68px;top:282px;width:166px;height:46px}

.contact-bg{top:2947px;left:0}
.signup{left:600px;top:0;width:600px;text-align:center;color:var(--white)}
.signup h2{position:absolute;top:3062px;width:600px;font-family:Barlow,Arial,sans-serif;font-weight:600;font-size:20px;color:var(--white)}
.signup .sub{position:absolute;top:3106px;width:600px;font-size:12px;font-weight:700}
.signup-form{position:absolute;top:3141px;left:69px;width:458px;height:46px;background:var(--white);border-radius:23px;overflow:hidden;display:flex;align-items:center;border:2px solid var(--white)}
.signup-form span{flex:1;text-align:left;padding-left:24px;font-size:11px;color:var(--ink)}
.signup-form b{width:136px;height:100%;background:var(--red);display:flex;align-items:center;justify-content:center;font-family:Barlow,Arial,sans-serif;font-weight:600;font-size:17px;border-radius:0 23px 23px 0}
.signup h3{position:absolute;width:600px;font-family:Barlow,Arial,sans-serif;font-weight:700;font-size:17px;color:var(--white)}
.hours{position:absolute;top:3243px;width:600px;font-size:13px;line-height:27.5px}
.social{position:absolute;top:3400px;left:249px;display:flex;gap:14px}
.social i{display:block;width:41px;height:41px;border-radius:50%}

.footer{top:3470px;left:0;width:1200px;height:461px;background:var(--black)}
.footer-logo{left:425px;top:3640px;width:350px;color:var(--white)}
.footer-logo .brand-name{font-size:26px;color:var(--white)}
.footer-logo .brand-tag{font-size:13px;color:var(--white);margin-top:14px;display:flex;align-items:center;gap:14px}
.footer-logo .brand-tag::before,.footer-logo .brand-tag::after{content:"";width:70px;height:1px;background:var(--white)}
.footer-nav{left:339px;top:3771px;color:var(--white);gap:46px}
.contacts{left:264px;top:3810px;display:flex;gap:46px;font-size:13px;align-items:center;color:var(--white)}
.contacts div{display:flex;align-items:center;gap:12px}
.contacts svg{width:37px;height:37px}
.copyright{top:3876px;left:0;width:1200px;text-align:center;font-size:12px;font-weight:700;color:var(--white)}
.copyright em{font-style:normal;color:var(--red)}
</style>
</head>
<body>

<div class="abs topbar">• OPEN WEDNESDAY-FRIDAY • 5-9PM • SATURDAY • 12-9PM • SUNDAY • 12-8PM • CLOSED MONDAYS &amp; TUESDAYS, THANKSGIVING, CHRISTMAS EVE &amp; CHRISTMAS DAY</div>

<header class="abs header">
  <div class="abs brand">
    <div class="brand-name"><i></i>Millbrook</div>
    <div class="brand-tag">Artisanal Pizza &amp; Craft Beer</div>
  </div>
  <nav class="abs nav"><span>Menu</span><span>Directions</span><span>Reservation</span><span>Take Out</span><span>Gift Cards</span></nav>
  <div class="btn phone-btn">207.555.0142</div>
</header>

<svg class="abs hero-bg" width="1200" height="630" viewBox="0 0 1200 630">
  <defs>
    <linearGradient id="facade" x1="0" y1="0" x2="1" y2="1">
      <stop offset="0" stop-color="#9fc3e6"/>
      <stop offset=".35" stop-color="#b6603f"/>
      <stop offset=".7" stop-color="#8d3e28"/>
      <stop offset="1" stop-color="#3b2a22"/>
    </linearGradient>
  </defs>
  <polygon points="0,100 600,0 600,622 0,516" fill="#d13a27"/>
  <polygon points="600,0 1200,76 1200,516 600,622" fill="url(#facade)" role="img" aria-label="Photo of the brick restaurant building with its sign and patio umbrellas"/>
  <g fill="none" stroke="#fff" stroke-width="1.5">
    <circle cx="600" cy="526" r="5"/><circle cx="600" cy="550" r="5" fill="#fff"/><circle cx="600" cy="574" r="5"/><circle cx="600" cy="598" r="5"/>
  </g>
</svg>
<h1 class="abs hero-title">Welcome to<br>Millbrook</h1>
<p class="abs hero-text">Lorem ipsum dolor sit amet, consectetur adipiscing elit, sed do eiusmod tempor incididunt ut labore et dolore magna aliqua. Ut enim ad minim veniam, quis nostrud exercitation ullamco</p>
<div class="btn btn-ghost hero-cta">Get Started</div>

<section class="about">
  <h2 class="heading">About Millbrook</h2>
  <div class="rule"></div>
  <p>Lorem ipsum dolor sit amet, consectetur adipiscing elit, sed do eiusmod tempor incididunt ut labore et dolore magna aliqua. Ut enim ad minim veniam, quis nostrud exercitation ullamco laboris nisi ut aliquip ex ea commodo consequat. Duis aute irure dolor in reprehenderit in voluptate velit esse cillum dolore eu fugiat nulla pariatur. Excepteur sint occaecat cupidatat non proident, sunt in culpa qui officia deserunt mollit anim id est laborum Sed ut perspiciatis unde omnis iste natus error sit voluptatem accusantium doloremque laudantium, totam rem aperiam, eaque ipsa quae ab illo inventore veritatis et quasi architecto beatae vitae dicta sunt explicabo. Nemo enim ipsam voluptatem quia voluptas sit aspernatur aut odit aut fugit sed quia consequuntur.</p>
  <div class="btn about-cta">Learn More</div>
</section>

<svg class="abs band-bg" width="1200" height="530" viewBox="0 0 1200 530">
  <defs>
    <linearGradient id="pizzaPhoto" x1="0" y1="0" x2="1" y2="1">
      <stop offset="0" stop-color="#4a3224"/><stop offset=".5" stop-color="#2f2119"/><stop offset="1" stop-color="#1d1510"/>
    </linearGradient>
    <linearGradient id="ovenPhoto" x1="0" y1="0" x2="0" y2="1">
      <stop offset="0" stop-color="#d7432d"/><stop offset=".6" stop-color="#c8321f"/><stop offset="1" stop-color="#a9261a"/>
    </linearGradient>
  </defs>
  <polygon points="0,3 600,77 600,451 0,524" fill="url(#pizzaPhoto)" role="img" aria-label="Dim close-up photo of a stone oven pizza"/>
  <polygon points="600,77 1200,3 1200,524 600,451" fill="url(#ovenPhoto)" role="img" aria-label="Red-toned photo of the wood-fired oven with hanging herbs"/>
</svg>
<div class="band-col band-left">
  <h2>Order Take Out</h2>
  <p>Sed ut perspiciatis unde omnis iste natus error sit voluptatem accusantium doloremque laudantium, totam rem aperiam, eaque ipsa quae ab illo inventore veritatis et quasi architecto beatae vitae dicta sunt explicabo. Nemo enim ipsam voluptatem quia voluptas sit aspernatur aut odit aut fugit, sed quia consequuntur omnis iste natus error sit voluptatem accusantium doloremque.</p>
</div>
<div class="btn btn-ghost band-btn" style="left:212px">Order Online</div>
<div class="band-col band-right">
  <h2>Artisanal Pizza &amp; Craft Beer</h2>
  <p>Sed ut perspiciatis unde omnis iste natus error sit voluptatem accusantium doloremque laudantium, totam rem aperiam, eaque ipsa quae ab illo inventore veritatis et quasi architecto beatae vitae dicta sunt explicabo. Nemo enim ipsam voluptatem quia voluptas sit aspernatur aut odit aut fugit, sed quia consequuntur omnis iste natus error sit voluptatem accusantium doloremque.</p>
</div>
<div class="btn btn-ghost band-btn" style="left:820px">View Menu</div>

<section class="career">
  <h2 class="heading">Career</h2>
  <div class="rule"></div>
  <p>Lorem ipsum dolor sit amet, consectetur adipiscing elit, sed do eiusmod tempor incididunt ut labore et dolore magna aliqua. Ut enim ad minim veniam, quis nostrud exercitation ullamco laboris nisi ut aliquip ex ea commodo consequat. Duis aute irure dolor in reprehenderit in voluptate velit esse cillum dolore eu fugiat nulla pariatur. Excepteur sint occaecat cupidatat non proident, sunt in culpa qui officia deserunt mollit anim id est laborum Sed ut perspiciatis unde omnis iste natus error sit voluptatem accusantium doloremque laudantium, totam rem aperiam, eaque ipsa quae ab illo inventore veritatis et quasi architecto beatae vitae dicta sunt explicabo. Nemo enim ipsam voluptatemq.</p>
  <div class="btn career-cta">Join Now</div>
  <div class="abs career-frame"></div>
  <div class="abs career-photo" role="img" aria-label="Photo of a pale lager and a dark stout on the bar"></div>
</section>

<div class="abs locations-bg" role="img" aria-label="Faint background of pizza and kitchen sketches"></div>
<section class="locations">
  <h2 class="heading">Serving artisanal stone oven pizza and hand<br>selected local and imported craft beers since 2012.</h2>
  <div class="rule"></div>
  <p class="lead">Enjoy chef created pizza on our home made dough and savory apps and entrees inspired by the freshest ingredients – from our house made sausage to fresh Maine Lobster and local produce – all cooked in our stone oven and thoughtfully paired with craft beer for optimum flavor combinations.</p>
  <div class="card" style="left:130px">
    <div class="card-photo" role="img" aria-label="Photo of a lobster pizza" style="background:linear-gradient(135deg,#b86a3a,#e6c9a0 50%,#8a4a28)"></div>
    <h3>SEACLIFF, ME</h3>
    <div class="addr">114 Harbor Street, Seacliff, ME</div>
    <div class="btn">View Menu</div>
  </div>
  <div class="card" style="left:450px">
    <div class="card-photo" role="img" aria-label="Photo of the patio with red umbrellas" style="background:linear-gradient(180deg,#8fb07a,#c2493a 45%,#5d6d3b)"></div>
    <h3>RIVERTON, NH</h3>
    <div class="addr">52 Foundry Lane, Riverton, NH</div>
    <div class="btn">Visit Riverton</div>
  </div>
  <div class="card" style="left:771px">
    <div class="card-photo" role="img" aria-label="Photo of bottles on the bar shelves" style="background:linear-gradient(135deg,#3a2b22,#a07a4f 50%,#d9d4cc)"></div>
    <h3>GIFT CARDS</h3>
    <div class="addr">Any Location. Never Expire.</div>
    <div class="btn">(207) 555-0142</div>
  </div>
</section>

<div class="abs footer"></div>

<svg class="abs contact-bg" width="1200" height="615" viewBox="0 0 1200 615">
  <defs>
    <linearGradient id="wood" x1="0" y1="0" x2="1" y2="1">
      <stop offset="0" stop-color="#4b3020"/><stop offset=".5" stop-color="#5a3b27"/><stop offset="1" stop-color="#3c2618"/>
    </linearGradient>
  </defs>
  <polygon points="0,100 600,0 600,615 0,527" fill="#eceeef" role="img" aria-label="Street map showing the restaurant location"/>
  <polygon points="600,0 1200,100 1200,527 600,615" fill="url(#wood)" role="img" aria-label="Dark wood texture"/>
</svg>

<section class="abs signup">
  <h2>WELCOME. MAY WE TAKE YOUR EMAIL?</h2>
  <div class="sub">NEWS • UPDATES • SPECIALS • SERVED TO YOUR INBOX • AS ORDERED</div>
  <div class="signup-form"><span>Enter the email</span><b>SUBSCRIBE</b></div>
  <h3 style="top:3215px">HOURS</h3>
  <div class="hours">Open Wednesday-Friday 5-9PM •<br>Saturday • 12-9pm • Sunday • 12-8pm<br>CLOSED MONDAYS &amp; TUESDAYS,<br>THANKSGIVING, CHRISTMAS EVE &amp; CHRISTMAS DAY</div>
  <h3 style="top:3368px">STAY CONNECTED</h3>
  <div class="social"><i style="background:#3b5ba8"></i><i style="background:#34c38a"></i></div>
</section>

<div class="abs brand footer-logo">
  <div class="brand-name">Millbrook</div>
  <div class="brand-tag">Artisanal Pizza &amp; Craft Beer</div>
</div>
<nav class="abs nav footer-nav"><span>Menu</span><span>Directions</span><span>Reservation</span><span>Take Out</span><span>Gift Cards</span></nav>
<div class="abs contacts">
  <div>
    <svg viewBox="0 0 40 40"><circle cx="20" cy="20" r="19" fill="#fff"/><path d="M20 9c-4.4 0-8 3.4-8 7.8C12 22.6 20 31 20 31s8-8.4 8-14.2C28 12.4 24.4 9 20 9z" fill="#d13a27"/><circle cx="20" cy="17" r="3" fill="#fff"/></svg>
    <span>114 Harbor Street, Seacliff, ME</span>
  </div>
  <div>
    <svg viewBox="0 0 40 40"><circle cx="20" cy="20" r="19" fill="#fff"/><path d="M14 11l4 0 2 5-2.5 2c1 2.2 2.8 4 5 5l2-2.5 5 2v4c0 1-1 2-2 2C19 28.5 11.5 21 11 13c0-1 1-2 2-2z" fill="#d13a27"/></svg>
    <span>207-555-0142</span>
  </div>
  <div>
    <svg viewBox="0 0 40 40"><circle cx="20" cy="20" r="19" fill="#fff"/><rect x="10" y="13" width="20" height="14" rx="1.5" fill="#d13a27"/><path d="M10.5 13.5L20 21l9.5-7.5" fill="none" stroke="#fff" stroke-width="1.5"/></svg>
    <span>hello@millbrookpizza-example.com</span>
  </div>
</div>
<div class="abs copyright">© COPYRIGHTS 2022 <em>MILLBROOK</em> | ALL RIGHTS RESERVED</div>

</body>
</html>
```